Postcard Design

Landscaping Company
Lawn Cuts
Mulch
Spring Clean Ups
Planting

Company Name - RTM GROUNDWORK SERVICES
ADDRESS - 47 Dunmore Ln.
W. Pellston, NJ 08591
Phone #- 609-555-0148

Target Market(s)

Direct mailer looking to draw in new clients

Industry/Entity Type

It Company

Requirements
Must have
• Eye catching

```html
<!DOCTYPE html>
<html lang="en">
<head>
<meta charset="UTF-8">
<title>RTM Groundwork Services — Postcard</title>
<link rel="stylesheet" href="https://fonts.googleapis.com/css2?family=Montserrat:wght@300;400;600;700&display=swap">
<style>
  :root {
    --brand-green: #0c9444;
    --page-bg: #ebecee;
    --body-top: #d3dbc7;
    --body-bottom: #f4f5f2;
    --ink: #111111;
    --ink-soft: #2a2a2a;
    --white: #ffffff;
    --grass-dark: #1f4a1a;
    --grass-mid: #3f7f2b;
    --grass-light: #7fb35a;
  }
  * { margin: 0; padding: 0; box-sizing: border-box; }
  html, body {
    width: 1200px; height: 1000px; overflow: hidden;
    background: var(--page-bg);
    font-family: "Montserrat", Arial, sans-serif;
  }
  .postcard {
    position: absolute; left: 255px; top: 51px;
    width: 690px; height: 898px;
    background: linear-gradient(180deg, var(--body-top) 0%, var(--body-bottom) 70%);
    overflow: hidden;
  }
  .postcard-header {
    position: absolute; left: 0; top: 0; width: 100%; height: 243px;
    background: var(--brand-green); color: var(--white);
    text-align: center; padding-top: 44px;
  }
  .company-name {
    font-weight: 700; font-size: 56px; line-height: 1; letter-spacing: -0.5px;
  }
  .company-name-sub {
    display: block; font-size: 46px; margin-top: 6px; font-weight: 600;
  }
  .company-address {
    font-weight: 600; font-size: 25px; margin-top: 18px;
  }
  .services {
    position: absolute; left: 58px; top: 292px; color: var(--ink);
  }
  .services-title {
    font-weight: 700; font-size: 31px; letter-spacing: 0.5px; margin-bottom: 14px;
  }
  .services-list { list-style: none; }
  .services-list li {
    font-weight: 300; font-size: 34px; line-height: 49px; color: var(--ink-soft);
    padding-left: 36px; position: relative;
  }
  .services-list li svg {
    position: absolute; left: 2px; top: 16px; width: 14px; height: 18px;
  }
  .slogan-box {
    position: absolute; left: 461px; top: 254px; width: 199px; height: 426px;
    background: var(--brand-green); color: var(--white);
    padding: 64px 0 0 15px;
    font-weight: 700; text-transform: uppercase; line-height: 0.98;
  }
  .slogan-box span { display: block; }
  .slogan-sm { font-size: 36px; }
  .slogan-lg { font-size: 46px; }
  .slogan-xs { font-size: 32px; }
  .grass-strip {
    position: absolute; left: 0; top: 660px; width: 100%; height: 146px;
    background: linear-gradient(180deg, rgba(127,179,90,0) 0%, var(--grass-light) 30%, var(--grass-mid) 65%, var(--grass-dark) 100%);
  }
  .postcard-footer {
    position: absolute; left: 0; top: 806px; width: 100%; height: 92px;
    background: var(--brand-green); color: var(--white);
    display: flex; align-items: center; justify-content: center;
    font-weight: 700; font-size: 31px;
  }
  .footer-divider {
    width: 3px; height: 58px; background: var(--white); margin: 0 14px;
  }
  .footer-phone { font-weight: 600; }
</style>
</head>
<body>
  <div class="postcard">
    <header class="postcard-header">
      <h1 class="company-name">RTM GROUNDWORK<span class="company-name-sub">SERVICES</span></h1>
      <p class="company-address">47 Dunmore Ln. W. Pellston, NJ 08591</p>
    </header>

    <section class="services">
      <h2 class="services-title">WHAT DO WE DO?</h2>
      <ul class="services-list">
        <li><svg viewBox="0 0 14 18"><polyline points="2,2 11,9 2,16" fill="none" stroke="#111" stroke-width="2"/></svg>Landscape</li>
        <li><svg viewBox="0 0 14 18"><polyline points="2,2 11,9 2,16" fill="none" stroke="#111" stroke-width="2"/></svg>Lawn Cuts</li>
        <li><svg viewBox="0 0 14 18"><polyline points="2,2 11,9 2,16" fill="none" stroke="#111" stroke-width="2"/></svg>Mulch</li>
        <li><svg viewBox="0 0 14 18"><polyline points="2,2 11,9 2,16" fill="none" stroke="#111" stroke-width="2"/></svg>Spring Clean Ups</li>
        <li><svg viewBox="0 0 14 18"><polyline points="2,2 11,9 2,16" fill="none" stroke="#111" stroke-width="2"/></svg>Planting</li>
      </ul>
    </section>

    <aside class="slogan-box">
      <span class="slogan-sm">A</span>
      <span class="slogan-sm">Happy</span>
      <span class="slogan-lg">Home</span>
      <span class="slogan-xs">Needs</span>
      <span class="slogan-sm">A</span>
      <span class="slogan-sm">Happy</span>
      <span class="slogan-lg">Yards</span>
    </aside>

    <div class="grass-strip" role="img" aria-label="Illustration of green grass blades and small leaves along the bottom edge"></div>

    <footer class="postcard-footer">
      <span class="footer-cta">CALL NOW!</span>
      <span class="footer-divider"></span>
      <span class="footer-phone">609-555-0148</span>
    </footer>
  </div>
</body>
</html>
```